M25 Billboard Advert Required Please

I need an advert for a motorway Billboard on the M25 , the advert should show the following in big letters:
GUTTER CLEANING
TOMSDRAINWORKS.NET and a small logo off to the side (Our logo is attached)

The printer has requested the following (Important please) the advert has to be
pdf file / 300 dpi/landscape orientation / scaled to a minimum 25% advert size ( this particular site is 22ft x 10ft so 25% of this please). Please also make sure that the artwork is embedded and outlined correctly if this is incorrect it will affect the printing of the banner.
Updates

Need extra days to review

Target Market(s)

General Public

Industry/Entity Type

Gutter Cleaning

Requirements
Should not have
• No Change to our Logo

```html
<!DOCTYPE html>
<html lang="en">
<head>
<meta charset="UTF-8">
<title>Gutter Cleaning Billboard – Tom's Drainworks</title>
<link href="https://fonts.googleapis.com/css2?family=Bebas+Neue&family=Poppins:wght@600&display=swap" rel="stylesheet">
<style>
  :root {
    --backdrop: #cfcfcf;
    --board: #ffffff;
    --brand-red: #b1252b;
    --ink: #111111;
    --shadow: rgba(0, 0, 0, 0.35);
  }
  * { margin: 0; padding: 0; box-sizing: border-box; }
  html, body {
    width: 970px;
    height: 1200px;
    overflow: hidden;
    background: var(--backdrop);
  }
  .canvas {
    position: relative;
    width: 970px;
    height: 1200px;
    background: var(--backdrop);
  }
  .billboard {
    position: absolute;
    left: 40px;
    top: 395px;
    width: 890px;
    height: 404px;
    background: var(--board);
    box-shadow: 6px 6px 10px var(--shadow);
  }
  .rule {
    position: absolute;
    left: 0;
    top: 87px;
    width: 772px;
    height: 2px;
    background: var(--brand-red);
  }
  .brand {
    position: absolute;
    right: 30px;
    top: 64px;
    display: flex;
    align-items: center;
    gap: 6px;
  }
  .brand-mark {
    width: 12px;
    height: 12px;
    background: var(--brand-red);
  }
  .brand-name {
    font-family: 'Poppins', sans-serif;
    font-weight: 600;
    font-size: 13px;
    color: var(--brand-red);
    white-space: nowrap;
  }
  .headline {
    position: absolute;
    left: 0;
    right: 0;
    top: 128px;
    text-align: center;
    font-family: 'Bebas Neue', sans-serif;
    font-size: 140px;
    line-height: 1;
    color: var(--brand-red);
    white-space: nowrap;
  }
  .web-address {
    position: absolute;
    left: 0;
    right: 0;
    top: 236px;
    text-align: center;
    font-family: 'Poppins', sans-serif;
    font-weight: 600;
    font-size: 76px;
    line-height: 1.2;
    letter-spacing: -1px;
    color: var(--ink);
    white-space: nowrap;
  }
</style>
</head>
<body>
  <main class="canvas">
    <section class="billboard">
      <div class="rule"></div>
      <div class="brand">
        <span class="brand-mark"></span>
        <span class="brand-name">Tom's Drainworks</span>
      </div>
      <h1 class="headline">GUTTER CLEANING!</h1>
      <p class="web-address">tomsdrainworks.net</p>
    </section>
  </main>
</body>
</html>
```